Business card design for strategy and management consulting company. Would like to have a clean and professional business card, based on the attached logo. The company is a strategy and management consulting company focusing on sustainable business modlels based on economic, social and environmental market opportunities. Preferably the logo should be included on both sides of the design.

Industry/Entity Type

Business

Contact Information for Business Card

Håvard Lilleby, CEO/Management consultant
havard.lilleby@quarvenpartners.example
Mob: +47 948 26 317
Office: Vikfjell gate 14, pb 312 sentrum, N-0172 Oslo Norway

Requirements
Must have
• Include attached logo
Nice to have
• Would like to have the logo on both sides
Should not have
• Many colours.

```html
<!DOCTYPE html>
<html lang="en">
<head>
<meta charset="utf-8">
<title>Quarven business card</title>
<link rel="stylesheet" href="https://fonts.googleapis.com/css2?family=Lato:wght@400;700;900&display=swap">
<style>
  :root {
    --backdrop: #2b2b2d;
    --card: #0b0f1a;
    --white: #ffffff;
    --gold: #f2be1a;
    --rule: #7a6420;
  }
  * { margin: 0; padding: 0; box-sizing: border-box; }
  html, body {
    width: 1200px;
    height: 900px;
    overflow: hidden;
    background: var(--backdrop);
    font-family: "Lato", Arial, sans-serif;
  }
  .canvas {
    position: relative;
    width: 1200px;
    height: 900px;
  }
  .card {
    position: absolute;
    left: 250px;
    width: 700px;
    height: 400px;
    background: var(--card);
    box-shadow: 0 10px 28px rgba(0, 0, 0, 0.45);
    overflow: hidden;
  }
  .card--front { top: 35px; }
  .card--back { top: 465px; }

  .wordmark {
    position: absolute;
    color: var(--white);
    font-weight: 700;
    letter-spacing: -1px;
    line-height: 1;
    white-space: nowrap;
  }
  .card--front .wordmark {
    left: 50%;
    top: 50%;
    transform: translate(-50%, -50%);
    font-size: 92px;
  }
  .card--back .wordmark {
    left: 58px;
    top: 172px;
    font-size: 64px;
  }

  .divider {
    position: absolute;
    left: 350px;
    top: 70px;
    width: 1px;
    height: 260px;
    background: var(--rule);
  }
  .contact {
    position: absolute;
    left: 378px;
    top: 82px;
    right: 20px;
    color: var(--white);
  }
  .contact__name {
    color: var(--gold);
    font-weight: 900;
    font-size: 25px;
    text-transform: uppercase;
    letter-spacing: 0.3px;
  }
  .contact__role {
    font-size: 11px;
    text-transform: uppercase;
    letter-spacing: 0.4px;
    margin-top: 3px;
  }
  .contact__address {
    font-size: 15px;
    line-height: 1.3;
    margin-top: 26px;
  }
  .contact__phone,
  .contact__email {
    color: var(--gold);
    font-size: 15px;
    font-weight: 700;
  }
  .contact__phone { margin-top: 34px; }
  .contact__email { margin-top: 22px; }
</style>
</head>
<body>
<main class="canvas">
  <section class="card card--front" aria-label="Card front">
    <div class="wordmark">Quarven</div>
  </section>

  <section class="card card--back" aria-label="Card back">
    <div class="wordmark">Quarven</div>
    <div class="divider"></div>
    <div class="contact">
      <p class="contact__name">Håvard Lilleby</p>
      <p class="contact__role">CEO/Management consultant</p>
      <p class="contact__address">Vikfjell gate 14,<br>pb 312 sentrum, Oslo Norway</p>
      <p class="contact__phone">+47 948 26 317</p>
      <p class="contact__email">havard.lilleby@quarvenpartners.example</p>
    </div>
  </section>
</main>
</body>
</html>
```